Dog Grooming Provisions - Coat Revival Mist *

We are Moss Hollow Meadows. A city dog's country camp. We are a dog services company providing a camp experience in Upstate NY to the dogs of NYC. We are creating a hand made Coat Revival Mist for our clients (who are dogs!) for the holidays.
These labels will be used on a 4 ounce vintage style spray bottles. The design should have a vintage grooming provisions feel. We'd like to see the design be a simple, vintage style black with white, charcoal, or very dark almost black green.
The design should incorporate our varying vintage fonts, our logo with "grooming provisions" all natural & handmade, Coat Revive
Obviously this is a gift and while Coat Revive is important, our brand should be a focus. Perhaps a very simple and "elegant" bone but steer away from paws and pet cheesy! Classic, vintage and camp.

Target Market(s)

Upscale Pet Owners of NYC

Industry/Entity Type

Pet Care

Logo Text

Moss Hollow Meadows Dog Camp (Dog Camp is is for logo not necessary for label)

Font styles to use
Serif
Sans Serif
Script

Colors
9bcb3b
000000
5c5c5c

Requirements
Must have
• I am looking for a black and white or very simple design. I'd even like our logo for this use be black/white (if possible? - not sure if that can happen?)
• Our branding! Simple vintage feel.
• Grooming Provisions
• Coat Revival or Coat Revive or Coat Bright Mist
• Handmade
• All Natural
• Fonts of vintage style - varying with simple and bold (i attached some photos)
Nice to have
• **MAYBE a very Simple Bone (see drawing) - very very thin.
Should not have
• 1. PAWS or cheap looking dog related items
• 2. No bright colors - truly prefer black and white or black with intention to print on plain pulp/brown paper (attached photo)
• 3. Over designed

```html
<!DOCTYPE html>
<html lang="en">
<head>
<meta charset="utf-8">
<title>Coat Revive Label</title>
<link rel="stylesheet" href="https://fonts.googleapis.com/css2?family=Rye&family=Kaushan+Script&family=Josefin+Sans:wght@400;600&display=swap">
<style>
  :root {
    --page: #e6e6e6;
    --label-light: #2e5a2d;
    --label-mid: #1a3a1b;
    --label-dark: #0a170b;
    --ink: #f1f1ec;
    --ink-soft: #d8ddd6;
  }
  * { margin: 0; padding: 0; box-sizing: border-box; }
  html, body { width: 1200px; height: 908px; overflow: hidden; }
  body {
    background: radial-gradient(ellipse at 50% 40%, #f6f6f6 0%, var(--page) 70%, #d6d6d6 100%);
    position: relative;
    font-family: "Josefin Sans", sans-serif;
  }
  .label {
    position: absolute;
    left: 210px; top: 44px;
    width: 780px; height: 820px;
    border-radius: 22px;
    background: radial-gradient(ellipse at 50% 38%, var(--label-light) 0%, var(--label-mid) 45%, var(--label-dark) 100%);
    box-shadow: 0 6px 18px rgba(0,0,0,0.25);
    color: var(--ink);
    text-align: center;
  }
  .frame-outer { position: absolute; inset: 20px; border: 2px solid var(--ink); }
  .frame-inner { position: absolute; inset: 30px; border: 1px solid var(--ink-soft); }
  .corner {
    position: absolute;
    width: 40px; height: 40px;
    background: var(--ink);
    opacity: 0.85;
    border-radius: 4px;
  }
  .corner.tl { left: 34px; top: 34px; }
  .corner.tr { right: 34px; top: 34px; }
  .corner.bl { left: 34px; bottom: 34px; }
  .corner.br { right: 34px; bottom: 34px; }
  .brand-mark {
    position: absolute;
    left: 50%; top: 88px;
    width: 72px; height: 72px;
    margin-left: -36px;
    border: 2px solid var(--ink);
    border-radius: 50%;
  }
  .brand-rule { position: absolute; top: 123px; height: 1px; width: 120px; background: var(--ink); }
  .brand-rule.left { left: 232px; }
  .brand-rule.right { right: 232px; }
  .brand-name {
    position: absolute;
    left: 0; right: 0; top: 226px;
    font-family: "Kaushan Script", cursive;
    font-size: 50px;
    line-height: 1;
    font-weight: 400;
    color: var(--ink);
  }
  .provisions { position: absolute; left: 0; right: 0; top: 372px; height: 36px; }
  .provisions-rules { position: absolute; left: 0; top: 0; }
  .provisions-box {
    position: absolute;
    left: 260px; top: 4px;
    width: 260px; height: 28px;
    border: 1.5px solid var(--ink);
    display: flex; align-items: center; justify-content: center; gap: 6px;
    font-size: 17px; letter-spacing: 1px;
    padding-top: 3px;
  }
  .bone { display: block; margin-top: -3px; flex: none; }
  .title {
    position: absolute;
    left: 0; right: 0; top: 422px;
    font-family: "Rye", serif;
    font-size: 76px;
    font-weight: 400;
    line-height: 1;
    letter-spacing: 3px;
    color: var(--ink-soft);
    text-transform: uppercase;
    white-space: nowrap;
  }
  .claims {
    position: absolute;
    left: 0; right: 0; top: 590px;
    font-family: "Kaushan Script", cursive;
    font-size: 34px;
    line-height: 1.1;
    display: flex; justify-content: center; align-items: center; gap: 12px;
  }
  .claims svg { display: block; }
  .divider {
    position: absolute;
    left: 220px; right: 220px; top: 668px;
    height: 1.5px;
    background: var(--ink);
  }
  .divider::before, .divider::after {
    content: ""; position: absolute; top: -3px;
    width: 7px; height: 7px; border-radius: 50%; background: var(--ink);
  }
  .divider::before { left: -10px; }
  .divider::after { right: -10px; }
  .established {
    position: absolute;
    left: 50%; top: 702px;
    width: 130px; height: 34px;
    margin-left: -65px;
    border: 1.5px solid var(--ink);
    font-size: 20px; letter-spacing: 2px;
    display: flex; align-items: center; justify-content: center;
    padding-top: 3px;
  }
</style>
</head>
<body>
  <main class="label">
    <div class="frame-outer"></div>
    <div class="frame-inner"></div>
    <div class="corner tl" role="img" aria-label="Corner flourish ornament"></div>
    <div class="corner tr" role="img" aria-label="Corner flourish ornament"></div>
    <div class="corner bl" role="img" aria-label="Corner flourish ornament"></div>
    <div class="corner br" role="img" aria-label="Corner flourish ornament"></div>

    <div class="brand-rule left"></div>
    <div class="brand-mark"></div>
    <div class="brand-rule right"></div>
    <h1 class="brand-name">Moss Hollow Meadows</h1>

    <div class="provisions">
      <svg class="provisions-rules" width="780" height="36" viewBox="0 0 780 36">
        <line x1="175" y1="18" x2="252" y2="18" stroke="#f1f1ec" stroke-width="1.5"/>
        <circle cx="170" cy="18" r="3" fill="#f1f1ec"/>
        <line x1="528" y1="18" x2="605" y2="18" stroke="#f1f1ec" stroke-width="1.5"/>
        <circle cx="610" cy="18" r="3" fill="#f1f1ec"/>
      </svg>
      <div class="provisions-box">
        <span>Grooming</span>
        <svg class="bone" width="26" height="8" viewBox="0 0 26 8"><line x1="3" y1="4" x2="23" y2="4" stroke="#f1f1ec" stroke-width="1.2"/><circle cx="3" cy="2.5" r="2" fill="none" stroke="#f1f1ec"/><circle cx="3" cy="5.5" r="2" fill="none" stroke="#f1f1ec"/><circle cx="23" cy="2.5" r="2" fill="none" stroke="#f1f1ec"/><circle cx="23" cy="5.5" r="2" fill="none" stroke="#f1f1ec"/></svg>
        <span>Provisions</span>
      </div>
    </div>

    <h2 class="title">Coat Revive</h2>

    <p class="claims">
      <span>Handmade</span>
      <svg width="22" height="20" viewBox="0 0 22 20"><path d="M11 18 C4 12 1 9 1 5.5 A4.5 4.5 0 0 1 11 4 A4.5 4.5 0 0 1 21 5.5 C21 9 18 12 11 18Z" fill="none" stroke="#f1f1ec" stroke-width="1.6"/></svg>
      <span>All Natural</span>
    </p>

    <div class="divider"></div>
    <div class="established">Est 2005</div>
  </main>
</body>
</html>
```